Flyer for Car Detailing Shop

I am opening a detailing shop. I am looking for a nice, easy to read single sided flyer I can hand out at car shows, hang in store windows and to my clients and customers to promote my business. I want it a little professional yet attention grabbing. I want someone to look at it and go "holy shit, thats a nice flyer" haha

Here are some things that must be included:
- Company Name: Brightfern Motorworks Detailing & Coatings
- Tag Line: The Science of Detailing
- Address: 4150 Harlow Rd, Temperance, MI 48190
- www.brightfernmotor.example
- Find Us on social Media! ::insert facebook and instagram logo
Colors: Black, Lime Green and Purple for accents, etc

HAND WASH
- Express Wash start at $25
- Deluxe Wash Start at $50

EXTERIOR DETAILING
-Basic Packages Start at $160
- Deluxe Packages Start at $350

INTERIOR DETAILING
- Basic Packages Start at $60
- Deluxe Packages Start at $200

New Car Prep and Ceramic Coatings
*Consultation required prior to beginning work*
- Paint: Starting at $500
- Interior: Starting at $100
- Wheels Off: Starting at $200
- Trim: Starting at $100
- Windows: $50 windshield/ $25 per pane

Additional Services
- Scratch removal
- Ozone Treatment
- Headlight Restoration
- Chip Repair

```html
<!DOCTYPE html>
<html lang="en">
<head>
<meta charset="utf-8">
<title>Brightfern Motorworks Flyer</title>
<link rel="stylesheet" href="https://fonts.googleapis.com/css2?family=League+Gothic&family=Didact+Gothic&display=swap">
<style>
:root{
  --stage:#808080;
  --lime:#a6f01f;
  --purple:#7e0f8c;
  --ink:#1b1b1b;
  --paper:#ffffff;
  --night:#050505;
  --photo-top:#9a9ea4;
  --photo-mid:#5b6068;
  --photo-low:#2c3036;
}
*{box-sizing:border-box;margin:0;padding:0}
html,body{width:1200px;height:818px;overflow:hidden;background:var(--stage)}
.stage{position:relative;width:1200px;height:818px}
.flyer{
  position:absolute;top:64px;width:533px;height:690px;overflow:hidden;
  background:var(--surface);color:var(--body);
  font-family:"Didact Gothic",sans-serif;
  --surface:var(--paper);--body:var(--ink);--head:var(--ink);--accent:var(--purple);--addr:var(--ink);
}
.flyer--light{left:58px}
.flyer--dark{left:609px;--surface:var(--night);--body:#fff;--head:var(--lime);--accent:#fff;--addr:var(--lime)}
.flyer--dark .backdrop{position:absolute;inset:0;background:radial-gradient(ellipse at 60% 45%,#262626 0%,#0b0b0b 55%,var(--night) 80%)}
.hero{position:absolute;left:0;top:0;width:533px;height:400px}
.title{position:absolute;left:34px;top:26px;font-family:"League Gothic",sans-serif;font-weight:400;color:var(--lime);line-height:63px;font-size:60px;white-space:nowrap}
.tagline{position:absolute;left:34px;top:152px;color:#fff;font-size:17px;letter-spacing:.4px}
.brand{position:absolute;left:330px;top:250px;width:180px;text-align:center;font-family:"League Gothic",sans-serif;font-size:28px;line-height:1.05;color:var(--head)}
.brand-dot{display:block;width:46px;height:46px;border-radius:50%;background:var(--head);margin:0 auto 8px}
.services{position:absolute;left:0;top:372px;width:533px}
.divider{position:absolute;left:267px;top:2px;width:1px;height:175px;background:#cfcfcf}
.flyer--dark .divider{background:#3a3a3a}
.item{position:absolute;left:38px}
.icon{position:absolute;left:0;top:6px;width:40px;height:32px;border-radius:8px;background:var(--lime)}
.item-body{position:absolute;left:54px;top:0;width:200px}
.head{font-family:"League Gothic",sans-serif;font-weight:400;color:var(--head);font-size:23px;line-height:24px;white-space:nowrap}
.line{font-size:8.6px;line-height:10.3px;white-space:nowrap}
.item .head{margin-bottom:2px}
.flyer--dark .item .price{color:#fff}
.flyer--light .item .price{color:var(--purple)}
.col{position:absolute;left:307px;width:210px}
.col .line{line-height:12.1px}
.label{color:var(--accent)}
.footer{position:absolute;left:38px;top:598px}
.footer-mark{position:absolute;left:0;top:0;width:46px;text-align:center;font-family:"League Gothic",sans-serif;font-size:9px;line-height:1.1;color:var(--head)}
.footer-mark .brand-dot{width:18px;height:18px;margin-bottom:3px}
.contact{position:absolute;left:54px;top:2px;font-size:8.6px;line-height:10px;white-space:nowrap}
.contact .addr{color:var(--addr)}
.socials{display:flex;gap:4px;margin-top:4px}
.social{width:14px;height:14px;border-radius:3px;background:var(--lime)}
.band{position:absolute;left:0;bottom:0;width:533px;height:9px;background:var(--lime)}
</style>
</head>
<body>
<main class="stage">

  <article class="flyer flyer--light">
    <svg class="hero" viewBox="0 0 533 400">
      <defs>
        <linearGradient id="photo-light" x1="0" y1="0" x2="0.3" y2="1">
          <stop offset="0" stop-color="#9a9ea4"/>
          <stop offset=".55" stop-color="#5b6068"/>
          <stop offset="1" stop-color="#2c3036"/>
        </linearGradient>
      </defs>
      <path role="img" aria-label="Photo of a detailer machine-polishing the bonnet of a silver car" fill="url(#photo-light)" d="M0 0H533V228C470 215 420 210 370 245C300 300 230 345 150 350C90 354 40 330 0 285Z"/>
      <path fill="#7e0f8c" d="M0 285C40 325 100 350 150 350C100 362 40 352 0 320Z"/>
      <path fill="#a6f01f" d="M125 360C230 362 300 310 360 262C410 222 460 200 533 196V212C470 214 420 232 380 265C310 325 240 368 125 360Z"/>
    </svg>
    <h1 class="title">Brightfern Motorworks<br>Detailing &amp; Coatings</h1>
    <p class="tagline">The Science of Detailing</p>
    <div class="brand"><span class="brand-dot"></span>Brightfern Motorworks</div>

    <section class="services">
      <div class="divider"></div>
      <div class="item" style="top:6px">
        <div class="icon" role="img" aria-label="Car wash icon"></div>
        <div class="item-body">
          <h2 class="head">HAND WASH</h2>
          <p class="line">Express Wash Start at <span class="price">$25</span></p>
          <p class="line">Deluxe Wash Start at <span class="price">$50</span></p>
        </div>
      </div>
      <div class="item" style="top:73px">
        <div class="icon" role="img" aria-label="Polishing hand icon"></div>
        <div class="item-body">
          <h2 class="head">EXTERIOR DETAILING</h2>
          <p class="line">Basic Packages Start at <span class="price">$160</span></p>
          <p class="line">Deluxe Packages Start at <span class="price">$350</span></p>
        </div>
      </div>
      <div class="item" style="top:140px">
        <div class="icon" role="img" aria-label="Vacuum hose icon"></div>
        <div class="item-body">
          <h2 class="head">INTERIOR DETAILING</h2>
          <p class="line">Basic Packages Start at <span class="price">$60</span></p>
          <p class="line">Deluxe Packages Start at <span class="price">$200</span></p>
        </div>
      </div>
      <div class="col" style="top:6px">
        <h2 class="head">New Car Prep and Ceramic Coatings</h2>
        <div style="margin-top:6px">
          <p class="line"><span class="label">Paint:</span> Starting at <span class="label">$500</span></p>
          <p class="line"><span class="label">Interior:</span> Starting at <span class="label">$100</span></p>
          <p class="line"><span class="label">Wheels Off:</span> Starting at <span class="label">$200</span></p>
          <p class="line"><span class="label">Trim:</span> Starting at <span class="label">$100</span></p>
          <p class="line"><span class="label">Windows:</span> <span class="label">$50</span> windshield/ <span class="label">$25</span> per pane</p>
        </div>
      </div>
      <div class="col" style="top:108px">
        <h2 class="head">Additional Services</h2>
        <div style="margin-top:6px">
          <p class="line">Scratch removal</p>
          <p class="line">Ozone Treatment</p>
          <p class="line">Headlight Restoration</p>
          <p class="line">Chip Repair</p>
        </div>
      </div>
    </section>

    <footer class="footer">
      <div class="footer-mark"><span class="brand-dot"></span>Brightfern Motorworks</div>
      <div class="contact">
        <p class="addr">4150 Harlow Rd, Temperance, MI 48190</p>
        <p>www.brightfernmotor.example</p>
        <p>Find Us on social Media!</p>
        <div class="socials"><span class="social"></span><span class="social"></span></div>
      </div>
    </footer>
    <div class="band"></div>
  </article>

  <article class="flyer flyer--dark">
    <div class="backdrop"></div>
    <svg class="hero" viewBox="0 0 533 400">
      <defs>
        <linearGradient id="photo-dark" x1="0" y1="0" x2="0.3" y2="1">
          <stop offset="0" stop-color="#9a9ea4"/>
          <stop offset=".55" stop-color="#5b6068"/>
          <stop offset="1" stop-color="#2c3036"/>
        </linearGradient>
      </defs>
      <path role="img" aria-label="Photo of a detailer machine-polishing the bonnet of a silver car" fill="url(#photo-dark)" d="M0 0H533V215C470 205 420 210 370 245C300 300 230 345 150 350C90 354 40 330 0 285Z"/>
      <path fill="#7e0f8c" d="M0 285C40 325 100 350 150 350C100 362 40 352 0 320Z"/>
      <path fill="#a6f01f" d="M125 360C230 362 300 310 360 262C410 222 460 200 533 196V212C470 214 420 232 380 265C310 325 240 368 125 360Z"/>
    </svg>
    <h1 class="title">Brightfern Motorworks<br>Detailing &amp; Coatings</h1>
    <p class="tagline">The Science of Detailing</p>
    <div class="brand"><span class="brand-dot"></span>Brightfern Motorworks</div>

    <section class="services">
      <div class="divider"></div>
      <div class="item" style="top:6px">
        <div class="icon" role="img" aria-label="Car wash icon"></div>
        <div class="item-body">
          <h2 class="head">HAND WASH</h2>
          <p class="line">Express Wash Start at <span class="price">$25</span></p>
          <p class="line">Deluxe Wash Start at <span class="price">$50</span></p>
        </div>
      </div>
      <div class="item" style="top:73px">
        <div class="icon" role="img" aria-label="Polishing hand icon"></div>
        <div class="item-body">
          <h2 class="head">EXTERIOR DETAILING</h2>
          <p class="line">Basic Packages Start at <span class="price">$160</span></p>
          <p class="line">Deluxe Packages Start at <span class="price">$350</span></p>
        </div>
      </div>
      <div class="item" style="top:140px">
        <div class="icon" role="img" aria-label="Vacuum hose icon"></div>
        <div class="item-body">
          <h2 class="head">INTERIOR DETAILING</h2>
          <p class="line">Basic Packages Start at <span class="price">$60</span></p>
          <p class="line">Deluxe Packages Start at <span class="price">$200</span></p>
        </div>
      </div>
      <div class="col" style="top:6px">
        <h2 class="head">New Car Prep and Ceramic Coatings</h2>
        <div style="margin-top:6px">
          <p class="line">Paint: Starting at $500</p>
          <p class="line">Interior: Starting at $100</p>
          <p class="line">Wheels Off: Starting at $200</p>
          <p class="line">Trim: Starting at $100</p>
          <p class="line">Windows: $50 windshield/ $25 per pane</p>
        </div>
      </div>
      <div class="col" style="top:108px">
        <h2 class="head">Additional Services</h2>
        <div style="margin-top:6px">
          <p class="line">Scratch removal</p>
          <p class="line">Ozone Treatment</p>
          <p class="line">Headlight Restoration</p>
          <p class="line">Chip Repair</p>
        </div>
      </div>
    </section>

    <footer class="footer">
      <div class="footer-mark"><span class="brand-dot"></span>Brightfern Motorworks</div>
      <div class="contact">
        <p class="addr">4150 Harlow Rd, Temperance, MI 48190</p>
        <p>www.brightfernmotor.example</p>
        <p>Find Us on social Media!</p>
        <div class="socials"><span class="social"></span><span class="social"></span></div>
      </div>
    </footer>
    <div class="band"></div>
  </article>

</main>
</body>
</html>
```